Luxury Car Hire business needs a website.

We need a sleek and elegant website for our luxury car hire business. It must have the following:
1. Homepage: We would like to include high-quality images of our luxury cars, a brief description of our business, and a clear call-to-action (CTA) to encourage visitors to explore further.
2. Car Listings: Create a dedicated section or page where visitors can browse our car fleet. Including high-resolution images, detailed descriptions of each car's features, specifications, pricing, availability, and any special offers or promotions.
3. Booking and Reservation System: We would like to implement HQ rentals booking system in our site.
4. Contact Information: Displaying contact details prominently, including phone number, email address, and a contact form. Also adding a live chat feature for real-time customer support.
5. About Us Page: A page for our company's story, mission, and values. Highlighting what sets our luxury car rental business apart from competitors.
6. Testimonials and Reviews: Showcase positive feedback and reviews from satisfied customers. This builds trust and credibility.
7. FAQs: Create a frequently asked questions section to address common queries about rental terms, insurance, pick-up and drop-off procedures, and more.
8. Blog: We would like to include a blog with articles related to luxury travel, car maintenance tips, destination guides, and other topics of interest to our target audience.
9. Gallery: Feature a gallery of stunning images and videos showcasing our cars in various scenic locations. This can help potential customers envision their experience.
10. Promotions and Special Offers: Dedicate a section to highlight current promotions, discounts, and package deals. Make sure to include expiration dates.
11. Safety and Policies: Clearly outline our safety measures, rental policies, insurance coverage, and terms and conditions.
12. Contact Forms: Besides the booking form, include contact forms for inquiries, feedback, and customer support.
13. Social Media Integration: Add social media links and sharing buttons to encourage visitors to follow your business on platforms like Chatterloop, Pictovia, and ZipZap.
14. Responsive Design: Ensure the website is mobile-friendly, as many users access websites via smartphones and tablets.
15. Search Functionality: Implement a search bar to help visitors quickly find specific car models or information.
16. Analytics and Tracking: Set up website analytics tools (e.g., Google Analytics) to monitor website traffic, user behaviour, and conversion rates.
Target Market(s)
Target affluent individuals aged 25-55. Mainly male demographic.
Coding
Coded - Design and coding required
Number of Pages Required
5+ page

```html
<!DOCTYPE html>
<html lang="en">
<head>
<meta charset="utf-8">
<title>Velaro — Luxury Car Hire</title>
<link href="https://fonts.googleapis.com/css2?family=Montserrat:wght@400;500;600;700;800&family=Mulish:wght@400;500;600;700&display=swap" rel="stylesheet">
<style>
:root{
  --black:#050505;
  --blue:#3347a8;
  --blue-deep:#2f3f9a;
  --light:#f4f2f3;
  --white:#ffffff;
  --ink:#111111;
  --muted:#6b6b6b;
}
*{box-sizing:border-box;margin:0;padding:0}
html,body{width:1200px;height:5367px;overflow:hidden}
body{font-family:'Mulish',sans-serif;color:var(--ink);background:var(--white);position:relative}
.section-title{font-family:'Montserrat',sans-serif;font-weight:700;font-size:24px;letter-spacing:3px;text-align:center;text-transform:uppercase}
.section-title::after{content:"";display:block;width:48px;height:3px;background:currentColor;margin:16px auto 0}
.btn{display:inline-block;background:var(--blue);color:var(--white);font-family:'Montserrat',sans-serif;font-weight:700;font-size:10px;letter-spacing:.5px;text-transform:uppercase;padding:9px 18px}
.ph{display:block}

/* Header */
.site-header{position:absolute;top:0;left:0;width:1200px;height:79px;background:var(--black);display:flex;align-items:center;justify-content:space-between;padding:0 131px}
.brand{font-family:'Montserrat',sans-serif;font-weight:500;font-size:20px;letter-spacing:3px;color:var(--white)}
.main-nav{display:flex;gap:28px}
.main-nav a{color:var(--white);font-family:'Montserrat',sans-serif;font-size:12px;font-weight:500;text-decoration:none;text-transform:uppercase}
.main-nav a.active{color:#5d74e0;text-decoration:underline}

/* Hero */
.hero{position:absolute;top:79px;left:0;width:1200px;height:531px;background:linear-gradient(180deg,#8b7466 0%,#5e4c44 40%,#3a302c 70%,#6d5a4c 100%)}
.hero-title{position:absolute;top:24px;width:100%;text-align:center;color:var(--white);font-family:'Montserrat',sans-serif;font-weight:700;font-size:38px;letter-spacing:4px;line-height:44px}
.hero .btn{position:absolute;left:519px;top:121px;width:162px;height:42px;font-size:16px;letter-spacing:2px;padding:0;line-height:42px;text-align:center}
.slide-arrow{position:absolute;width:26px;height:26px;border:1.5px solid currentColor;border-radius:50%;display:flex;align-items:center;justify-content:center}
.hero .slide-arrow{color:var(--white);top:245px}
.search-bar{position:absolute;top:579px;left:246px;width:708px;height:56px;background:var(--white);border:2px solid #222;display:flex;align-items:center;justify-content:space-between;padding:0 20px;z-index:2;font-family:'Montserrat',sans-serif;font-size:13px;font-weight:600}

/* Welcome */
.welcome{position:absolute;top:610px;left:0;width:1200px;height:507px}
.welcome .ph{position:absolute;left:0;top:0;width:569px;height:507px;background:linear-gradient(135deg,#7a1b1b 0%,#1a1a1e 45%,#2b2b30 70%,#88887f 100%)}
.welcome-copy{position:absolute;left:625px;top:95px;width:435px}
.welcome-copy h2{font-family:'Montserrat',sans-serif;font-weight:700;font-size:24px;letter-spacing:3px;margin-bottom:36px}
.welcome-copy p{font-size:13px;line-height:22px;color:var(--muted);text-align:justify;margin-bottom:30px}

/* Fleet */
.fleet{position:absolute;top:1117px;left:0;width:1200px;height:660px;background:var(--light)}
.fleet .section-title{position:absolute;top:48px;width:100%}
.card-row{position:absolute;left:131px;width:936px;display:flex;justify-content:space-between}
.fleet .card-row{top:139px}
.car-card{width:225px;height:417px;background:var(--white)}
.car-card .ph{height:202px;background:linear-gradient(160deg,#5a6470,#24282e)}
.car-card-body{padding:20px 22px}
.car-card h3{font-family:'Montserrat',sans-serif;font-size:12px;font-weight:600;margin-bottom:8px}
.car-card p{font-size:11px;line-height:14px;color:var(--muted)}
.price{font-family:'Montserrat',sans-serif;color:var(--blue-deep);font-weight:700;font-size:20px;margin:10px 0 12px}
.fleet .slide-arrow{color:var(--blue);top:329px}
.btn-outline{position:absolute;left:534px;top:589px;width:132px;height:31px;border:2px solid var(--blue);color:var(--blue-deep);font-family:'Montserrat',sans-serif;font-size:11px;font-weight:700;text-align:center;line-height:27px;text-transform:uppercase}

/* Offers */
.offers{position:absolute;top:1777px;left:0;width:1200px;height:483px;background:var(--black);color:var(--white)}
.offers .section-title{position:absolute;top:56px;width:100%}
.offer{position:absolute;top:127px;width:462px;height:310px}
.offer-a{left:131px;background:linear-gradient(180deg,#3a3f4c 0%,#a8683f 55%,#e99a2c 100%)}
.offer-b{left:606px;background:linear-gradient(120deg,#f5a11d 0%,#f29d1f 55%,#d4d4d4 100%)}

/* Gallery */
.gallery{position:absolute;top:2260px;left:0;width:1200px;height:683px}
.gallery .section-title{position:absolute;top:40px;width:100%}
.gallery-grid{position:absolute;top:121px;left:131px;width:936px;display:grid;grid-template-columns:repeat(4,225px);grid-template-rows:repeat(2,225px);gap:12px;justify-content:space-between}
.gallery-grid .ph{width:225px;height:225px}
.gallery .btn{position:absolute;top:608px;left:532px;width:136px;height:32px;padding:0;text-align:center;line-height:32px;font-size:11px}

/* Testimonials */
.testimonials{position:absolute;top:2943px;left:0;width:1200px;height:521px;background:var(--light)}
.testimonials .section-title{position:absolute;top:46px;width:100%}
.testimonials .card-row{top:134px}
.review{width:298px;height:331px;background:var(--white);border-bottom:4px solid var(--blue);text-align:center;padding:28px 30px 0}
.review p{font-size:12.5px;line-height:20px;color:var(--muted);margin:14px 0 16px}
.avatar{width:44px;height:44px;border-radius:50%;margin:0 auto 10px;background:linear-gradient(180deg,#e0b48c,#c9875a)}
.review h4{font-size:13px;font-weight:600}
.testimonials .slide-arrow{color:var(--ink);top:288px}

/* Blog */
.blog{position:absolute;top:3464px;left:0;width:1200px;height:608px}
.blog .section-title{position:absolute;top:56px;width:100%}
.blog .card-row{top:129px}
.post{width:298px;height:438px;background:var(--white);box-shadow:0 2px 14px rgba(0,0,0,.08)}
.post .ph{height:183px}
.post-body{padding:24px 28px}
.post time{font-size:11px;color:#333}
.post h3{font-family:'Montserrat',sans-serif;font-weight:600;font-size:13px;line-height:20px;margin:8px 0 12px}
.post p{font-size:12.5px;line-height:20px;color:var(--muted);margin-bottom:20px}

/* FAQ */
.faq{position:absolute;top:4072px;left:0;width:1200px;height:396px}
.faq .section-title{position:absolute;top:40px;width:100%}
.faq-list{position:absolute;top:112px;left:162px;width:792px;list-style:none}
.faq-list li{height:52px;border-bottom:2px solid var(--blue);display:flex;align-items:center;justify-content:space-between;padding:0 20px;color:var(--blue-deep);font-family:'Montserrat',sans-serif;font-weight:600;font-size:15px}

/* Contact */
.contact{position:absolute;top:4468px;left:0;width:1200px;height:531px;background:var(--blue-deep);color:var(--white)}
.contact .section-title{position:absolute;top:45px;width:100%}
.contact-form{position:absolute;top:146px;left:323px;width:552px}
.field{background:var(--white);border-radius:4px;height:40px;margin-bottom:14px;padding:12px 16px;font-size:12px;color:#555}
.field-pair{display:flex;gap:14px}
.field-pair .field{flex:1}
.field-message{height:107px}
.submit{position:absolute;top:298px;left:212px;width:125px;height:38px;border-radius:19px;background:var(--white);color:var(--blue-deep);font-family:'Montserrat',sans-serif;font-weight:700;font-size:16px;text-align:center;line-height:38px}

/* Footer */
.site-footer{position:absolute;top:4999px;left:0;width:1200px;height:368px;background:var(--black);color:var(--white)}
.footer-brand{position:absolute;left:131px;top:125px;font-family:'Montserrat',sans-serif;font-weight:500;font-size:28px;letter-spacing:4px}
.footer-col{position:absolute;top:44px}
.footer-col h4{font-family:'Montserrat',sans-serif;font-weight:700;font-size:13px;padding-bottom:10px;border-bottom:2px solid var(--white);margin-bottom:18px}
.col-contact{left:400px;width:196px}
.col-menu{left:710px;width:110px}
.col-follow{left:958px;width:110px}
.info-row{display:flex;gap:12px;align-items:flex-start;font-size:11px;line-height:14px;margin-bottom:22px}
.dot{flex:0 0 22px;height:22px;border-radius:50%;background:var(--blue);display:flex;align-items:center;justify-content:center}
.col-menu ul{list-style:none;font-size:11px;line-height:19px}
.footer-rule{position:absolute;top:271px;left:131px;width:936px;height:1px;background:#777}
.legal{position:absolute;top:311px;width:100%;text-align:center;font-size:10.5px}
</style>
</head>
<body>

<header class="site-header">
  <div class="brand">VELARO</div>
  <nav class="main-nav">
    <a class="active">Home</a><a>About Us</a><a>Cars</a><a>Testimonials</a><a>FAQs</a><a>Blog</a><a>Gallery</a><a>Contact Us</a>
  </nav>
</header>

<section class="hero" role="img" aria-label="Dark blue luxury coupe on a mountain road at sunset">
  <h1 class="hero-title">LUXURY CAR HIRE FOR<br>YOUR ULTIMATE JOURNEY</h1>
  <a class="btn">Book Now</a>
  <span class="slide-arrow" style="left:90px"><svg width="10" height="10" viewBox="0 0 10 10"><path d="M6.5 1.5 3 5l3.5 3.5" stroke="currentColor" stroke-width="1.6" fill="none"/></svg></span>
  <span class="slide-arrow" style="left:1073px"><svg width="10" height="10" viewBox="0 0 10 10"><path d="M3.5 1.5 7 5 3.5 8.5" stroke="currentColor" stroke-width="1.6" fill="none"/></svg></span>
</section>

<div class="search-bar"><span>SEARCH CAR</span>
  <svg width="20" height="20" viewBox="0 0 20 20"><circle cx="8" cy="8" r="6" stroke="#111" stroke-width="2" fill="none"/><path d="M12.5 12.5 18 18" stroke="#111" stroke-width="2"/></svg>
</div>

<section class="welcome">
  <div class="ph" role="img" aria-label="Black SUV driving with red light trails"></div>
  <div class="welcome-copy">
    <h2>WELCOME TO VELARO</h2>
    <p>Sed ut perspiciatis unde omnis iste natus error sit volupt atem accusantium doloremque laudantium, totam rem aperiam, eaque ipsa quae ab illo inventore veritatis et quasi architecto beatae vitae dicta sunt explicabo. Nemo enim ipsam voluptatem quia voluptas sit aspernatur aut odit aut fugit, sed quia cons equ untur magni dolores eos qui ratione voluptatem sequi nesciunt. Neque porro quisquam est, qui dolorem ipsum quia dolor sit ame</p>
    <a class="btn">Read More</a>
  </div>
</section>

<section class="fleet">
  <h2 class="section-title">Our Car Fleet</h2>
  <span class="slide-arrow" style="left:74px"><svg width="10" height="10" viewBox="0 0 10 10"><path d="M6.5 1.5 3 5l3.5 3.5" stroke="currentColor" stroke-width="1.6" fill="none"/></svg></span>
  <div class="card-row">
    <article class="car-card"><div class="ph" role="img" aria-label="Silver sedan on a wet road"></div><div class="car-card-body"><h3>CAR 1</h3><p>Sed ut perspiciatis unde omnis iste natus error sit volupt atem accusantium doloremque laud antium...</p><div class="price">$25.99</div><a class="btn">Read More</a></div></article>
    <article class="car-card"><div class="ph" role="img" aria-label="White sedan among autumn trees" style="background:linear-gradient(160deg,#b5571f,#e0d7cc)"></div><div class="car-card-body"><h3>CAR 2</h3><p>Sed ut perspiciatis unde omnis iste natus error sit volupt atem accusantium doloremque laud antium...</p><div class="price">$25.99</div><a class="btn">Read More</a></div></article>
    <article class="car-card"><div class="ph" role="img" aria-label="Dark blue coupe in a village street" style="background:linear-gradient(160deg,#c9a887,#2b3550)"></div><div class="car-card-body"><h3>CAR 3</h3><p>Sed ut perspiciatis unde omnis iste natus error sit volupt atem accusantium doloremque laud antium...</p><div class="price">$25.99</div><a class="btn">Read More</a></div></article>
    <article class="car-card"><div class="ph" role="img" aria-label="Black coupe in a grey studio" style="background:linear-gradient(160deg,#9a9a9a,#1a1a1a)"></div><div class="car-card-body"><h3>CAR 4</h3><p>Sed ut perspiciatis unde omnis iste natus error sit volupt atem accusantium doloremque laud antium...</p><div class="price">$25.99</div><a class="btn">Read More</a></div></article>
  </div>
  <span class="slide-arrow" style="left:1096px"><svg width="10" height="10" viewBox="0 0 10 10"><path d="M3.5 1.5 7 5 3.5 8.5" stroke="currentColor" stroke-width="1.6" fill="none"/></svg></span>
  <a class="btn-outline">View All Cars</a>
</section>

<section class="offers">
  <h2 class="section-title">Special Offers</h2>
  <div class="offer offer-a" role="img" aria-label="Promotional banner: luxury car, 40% off today, expiry 20 Oct 2023"></div>
  <div class="offer offer-b" role="img" aria-label="Promotional banner: best car rental deals, 40% off today, expiry 20 Oct 2023"></div>
</section>

<section class="gallery">
  <h2 class="section-title">Gallery</h2>
  <div class="gallery-grid">
    <div class="ph" role="img" aria-label="Classic muscle car reflected on a wet floor" style="background:linear-gradient(180deg,#9aa0a5,#1c1c1e)"></div>
    <div class="ph" role="img" aria-label="Blue sedan in a parking lot" style="background:linear-gradient(180deg,#6e8aa8,#4a5460)"></div>
    <div class="ph" role="img" aria-label="Green coupe on a cobbled street" style="background:linear-gradient(180deg,#c4854a,#3e4a3c)"></div>
    <div class="ph" role="img" aria-label="White estate car by a rock face" style="background:linear-gradient(180deg,#7a6252,#d9d7d3)"></div>
    <div class="ph" role="img" aria-label="Grey SUV in a green field" style="background:linear-gradient(180deg,#7ea4c6,#556b3e)"></div>
    <div class="ph" role="img" aria-label="Blue performance sedan front view" style="background:linear-gradient(180deg,#2a3242,#2c3a7a)"></div>
    <div class="ph" role="img" aria-label="White sports car by the sea" style="background:linear-gradient(180deg,#9fc0dc,#d8d2c4)"></div>
    <div class="ph" role="img" aria-label="Red sports car on paving" style="background:linear-gradient(180deg,#5a2a2a,#d0301f)"></div>
  </div>
  <a class="btn">View All Images</a>
</section>

<section class="testimonials">
  <h2 class="section-title">Testimonials</h2>
  <span class="slide-arrow" style="left:68px"><svg width="10" height="10" viewBox="0 0 10 10"><path d="M6.5 1.5 3 5l3.5 3.5" stroke="currentColor" stroke-width="1.6" fill="none"/></svg></span>
  <div class="card-row">
    <article class="review"><svg width="48" height="34" viewBox="0 0 48 34"><path d="M4 34V20C4 9 10 3 19 1l1 4c-6 2-8 6-8 11h8v18zM28 34V20c0-11 6-17 15-19l1 4c-6 2-8 6-8 11h8v18z" fill="#3347a8"/></svg><p>Sed ut perspiciatis unde omnis iste natus error sit voluptatem accus antium doloremque laudantium, totam rem aperiam, eaque ipsa quae ab illo inventore veritatis et quasi architecto beatae vitae dicta sunt.</p><div class="avatar" role="img" aria-label="Customer portrait"></div><h4>Marcus</h4></article>
    <article class="review"><svg width="48" height="34" viewBox="0 0 48 34"><path d="M4 34V20C4 9 10 3 19 1l1 4c-6 2-8 6-8 11h8v18zM28 34V20c0-11 6-17 15-19l1 4c-6 2-8 6-8 11h8v18z" fill="#3347a8"/></svg><p>Sed ut perspiciatis unde omnis iste natus error sit voluptatem accus antium doloremque laudantium, totam rem aperiam, eaque ipsa quae ab illo inventore veritatis et quasi architecto beatae vitae dicta sunt.</p><div class="avatar" role="img" aria-label="Customer portrait"></div><h4>Marcus</h4></article>
    <article class="review"><svg width="48" height="34" viewBox="0 0 48 34"><path d="M4 34V20C4 9 10 3 19 1l1 4c-6 2-8 6-8 11h8v18zM28 34V20c0-11 6-17 15-19l1 4c-6 2-8 6-8 11h8v18z" fill="#3347a8"/></svg><p>Sed ut perspiciatis unde omnis iste natus error sit voluptatem accus antium doloremque laudantium, totam rem aperiam, eaque ipsa quae ab illo inventore veritatis et quasi architecto beatae vitae dicta sunt.</p><div class="avatar" role="img" aria-label="Customer portrait"></div><h4>Marcus</h4></article>
  </div>
  <span class="slide-arrow" style="left:1098px"><svg width="10" height="10" viewBox="0 0 10 10"><path d="M3.5 1.5 7 5 3.5 8.5" stroke="currentColor" stroke-width="1.6" fill="none"/></svg></span>
</section>

<section class="blog">
  <h2 class="section-title">Latest Blog</h2>
  <div class="card-row">
    <article class="post"><div class="ph" role="img" aria-label="Silver SUV on a highway" style="background:linear-gradient(180deg,#c9ccd0,#6f7378)"></div><div class="post-body"><time>Oct 03, 2023</time><h3>Lorem ipsum dolor sit amet consectetur adipiscing</h3><p>Sed ut perspiciatis unde omnis iste natus error sit voluptatem accus antium doloremque laudantium, totam rem aperiam</p><a class="btn">Read More</a></div></article>
    <article class="post"><div class="ph" role="img" aria-label="Black sedan parked among trees" style="background:linear-gradient(180deg,#5f7a4c,#1e2226)"></div><div class="post-body"><time>Oct 03, 2023</time><h3>Lorem ipsum dolor sit amet consectetur adipiscing</h3><p>Sed ut perspiciatis unde omnis iste natus error sit voluptatem accus antium doloremque laudantium, totam rem aperiam</p><a class="btn">Read More</a></div></article>
    <article class="post"><div class="ph" role="img" aria-label="Car interior with steering wheel" style="background:linear-gradient(160deg,#1a1a1a,#8c8c8c)"></div><div class="post-body"><time>Oct 03, 2023</time><h3>Lorem ipsum dolor sit amet consectetur adipiscing</h3><p>Sed ut perspiciatis unde omnis iste natus error sit voluptatem accus antium doloremque laudantium, totam rem aperiam</p><a class="btn">Read More</a></div></article>
  </div>
</section>

<section class="faq">
  <h2 class="section-title">FAQ</h2>
  <ul class="faq-list">
    <li>What types of luxury cars do you offer for hire?<svg width="22" height="22" viewBox="0 0 22 22"><circle cx="11" cy="11" r="10" stroke="#3347a8" stroke-width="1.4" fill="none"/><path d="M7 9.5 11 13.5 15 9.5" stroke="#3347a8" stroke-width="1.4" fill="none"/></svg></li>
    <li>What are the rental rates for your luxury cars?<svg width="22" height="22" viewBox="0 0 22 22"><circle cx="11" cy="11" r="10" stroke="#3347a8" stroke-width="1.4" fill="none"/><path d="M7 9.5 11 13.5 15 9.5" stroke="#3347a8" stroke-width="1.4" fill="none"/></svg></li>
    <li>Are there any age or driver's license requirements to rent a luxury car?<svg width="22" height="22" viewBox="0 0 22 22"><circle cx="11" cy="11" r="10" stroke="#3347a8" stroke-width="1.4" fill="none"/><path d="M7 9.5 11 13.5 15 9.5" stroke="#3347a8" stroke-width="1.4" fill="none"/></svg></li>
    <li>Is insurance included with the luxury car rental?<svg width="22" height="22" viewBox="0 0 22 22"><circle cx="11" cy="11" r="10" stroke="#3347a8" stroke-width="1.4" fill="none"/><path d="M7 9.5 11 13.5 15 9.5" stroke="#3347a8" stroke-width="1.4" fill="none"/></svg></li>
    <li>Can I pick up and drop off the luxury car at different locations?<svg width="22" height="22" viewBox="0 0 22 22"><circle cx="11" cy="11" r="10" stroke="#3347a8" stroke-width="1.4" fill="none"/><path d="M7 9.5 11 13.5 15 9.5" stroke="#3347a8" stroke-width="1.4" fill="none"/></svg></li>
  </ul>
</section>

<section class="contact">
  <h2 class="section-title">Contact Us</h2>
  <form class="contact-form">
    <div class="field-pair"><div class="field">First Name</div><div class="field">Last Name</div></div>
    <div class="field">Email Id</div>
    <div class="field">Phone</div>
    <div class="field field-message">Message</div>
    <div class="submit">SUBMIT</div>
  </form>
</section>

<footer class="site-footer">
  <div class="footer-brand">VELARO</div>
  <div class="footer-col col-contact">
    <h4>CONTACT US</h4>
    <div class="info-row"><span class="dot"><svg width="10" height="12" viewBox="0 0 10 12"><path d="M5 11S1 6.5 1 4a4 4 0 0 1 8 0c0 2.5-4 7-4 7z" fill="#fff"/><circle cx="5" cy="4" r="1.4" fill="#3347a8"/></svg></span><span>48 Harbourline Ave, Northfield,<br>ON K2P 4R1, Canada</span></div>
    <div class="info-row"><span class="dot"><svg width="10" height="10" viewBox="0 0 10 10"><path d="M2 1l2 2-1 1.5c.6 1.2 1.3 1.9 2.5 2.5L7 6l2 2-1.5 1.5C4 9 1 6 .5 2.5z" fill="#fff"/></svg></span><span>Call Us<br>+1 555 010 2040</span></div>
    <div class="info-row"><span class="dot"><svg width="11" height="8" viewBox="0 0 11 8"><rect x=".5" y=".5" width="10" height="7" fill="#fff"/><path d="M.5.5 5.5 4.5 10.5.5" stroke="#3347a8" fill="none"/></svg></span><span>E mail Us<br>info@velaro.example</span></div>
  </div>
  <div class="footer-col col-menu">
    <h4>MENU</h4>
    <ul><li>Home</li><li>About Us</li><li>Cars</li><li>Testimonials</li><li>FAQs</li><li>Blog</li><li>Gallery</li><li>Contact Us</li></ul>
  </div>
  <div class="footer-col col-follow">
    <h4>FOLLOW US</h4>
    <div class="info-row"><span class="dot"></span><span>Like us on<br>CHATTERLOOP</span></div>
    <div class="info-row"><span class="dot"></span><span>Follow us on<br>PICTOVIA</span></div>
    <div class="info-row"><span class="dot"></span><span>Follow us on<br>ZIPZAP</span></div>
  </div>
  <div class="footer-rule"></div>
  <p class="legal">Privacy Policy &nbsp;|&nbsp; Terms and Conditions &nbsp;|&nbsp; Copyright © 2023 All Rights Reserved</p>
</footer>

</body>
</html>
```